IT Company Business Card Rebranding

We want to modernize our business cards massively. We want to incorporate aspects of our old business card such as the white and geometric design with the blues of another icon. Existing Logo, old business card and icon are all attached.

We are a modern IT company that provides support for new and growing technologies and want our business cards to be modern yet professional.
Updates

Note: Do not use file ICON.png in design. This is just a design we like Added Wednesday, March 9, 2016

Industry/Entity Type

Information Technology

Contact Information for Business Card

Roughly 43 : 26 or 1075 x 650 px

Font styles to use
Serif

Colors
0492cd
3276b5
33a6d7
86cfc6
cfeae6
cee9f5
ffffff

Requirements
Must have
• Modern yet professional
Nice to have
• We would like to incorporate the blues of our existing logo and of the icon provided. Really like the design of the icon.
Should not have
• Too Decorative. Just simple and professional.
• Not have the circle icon, as it is a copyrighted icon, I just like the colors and the geometric design

```html
<!DOCTYPE html>
<html lang="en">
<head>
<meta charset="utf-8">
<title>Kestrel IT – Business Cards</title>
<link rel="stylesheet" href="https://fonts.googleapis.com/css2?family=Open+Sans:wght@400;700&display=swap">
<style>
  :root {
    --page-bg: #eceae6;
    --card-white: #ffffff;
    --card-fade: #e6e7e9;
    --ink-blue: #1848b0;
    --ink-grey: #555a60;
    --brand-grey: #7d8086;
    --blue-deep: #1b4fc0;
    --blue-mid: #3276b5;
    --blue-bright: #0492cd;
    --blue-sky: #33a6d7;
    --blue-pale: #cee9f5;
    --blue-ice: #b9def3;
  }
  * { margin: 0; padding: 0; box-sizing: border-box; }
  html, body { width: 968px; height: 1200px; overflow: hidden; }
  body {
    background: var(--page-bg);
    font-family: "Open Sans", sans-serif;
    position: relative;
  }
  .card {
    position: absolute;
    left: 120px;
    width: 719px;
    height: 449px;
    overflow: hidden;
    box-shadow: 0 2px 6px rgba(0,0,0,.18);
  }
  .card--front {
    top: 108px;
    background: linear-gradient(150deg, var(--card-white) 30%, var(--card-fade) 100%);
  }
  .card--back {
    top: 643px;
    background: var(--card-white);
  }
  .card__art { position: absolute; inset: 0; }
  .brand {
    position: absolute;
    display: flex;
    align-items: center;
    gap: 12px;
    color: var(--brand-grey);
    font-size: 22px;
    font-weight: 400;
    letter-spacing: 6px;
    text-transform: uppercase;
  }
  .brand__mark {
    width: 16px; height: 16px;
    background: var(--blue-mid);
  }
  .card--front .brand { left: 52px; top: 110px; }
  .card--back .brand { left: 57px; top: 196px; }

  .holder { position: absolute; }
  .holder__name { color: var(--ink-blue); font-weight: 700; line-height: 1; }
  .holder__role { color: var(--ink-grey); line-height: 1; }
  .card--front .holder { left: 191px; top: 175px; }
  .card--front .holder__name { font-size: 25px; text-transform: uppercase; }
  .card--front .holder__role { font-size: 19px; margin-top: 12px; text-transform: uppercase; }
  .card--back .holder { right: 71px; top: 216px; text-align: right; }
  .card--back .holder__name { font-size: 26px; }
  .card--back .holder__role { font-size: 22px; margin-top: 10px; }

  .contacts { position: absolute; list-style: none; }
  .contacts li {
    display: flex;
    align-items: center;
    gap: 8px;
    height: 31px;
    font-size: 18px;
    color: var(--ink-grey);
  }
  .contacts svg { width: 18px; height: 18px; flex: none; }
  .card--front .contacts { left: 190px; top: 248px; }
  .card--back .contacts { left: 70px; top: 262px; }
</style>
</head>
<body>

<section class="card card--front" aria-label="Business card front">
  <svg class="card__art" viewBox="0 0 719 449" preserveAspectRatio="none">
    <defs>
      <linearGradient id="facets-front" x1="0" y1="0" x2="1" y2="1">
        <stop offset="0" stop-color="#d6ecf8"/>
        <stop offset=".5" stop-color="#7cc6ec"/>
        <stop offset="1" stop-color="#2f7fd8"/>
      </linearGradient>
      <linearGradient id="corner-band" x1="0" y1="0" x2="1" y2="0">
        <stop offset="0" stop-color="#2a6fc4"/>
        <stop offset=".5" stop-color="#10b0ea"/>
        <stop offset="1" stop-color="#1b3fb8"/>
      </linearGradient>
    </defs>
    <polygon role="img" aria-label="Blue low-poly geometric facets" fill="url(#facets-front)"
      points="265,0 369,48 463,79 608,183 660,277 719,329 719,0"/>
    <polygon fill="url(#corner-band)" points="0,334 78,399 328,449 0,449"/>
  </svg>

  <div class="brand"><span class="brand__mark"></span>Kestrel IT</div>

  <div class="holder">
    <p class="holder__name">Milo</p>
    <p class="holder__role">Technical Services</p>
  </div>

  <ul class="contacts">
    <li><svg viewBox="0 0 20 20"><path d="M5 2 L8 2 L9 6 L7 8 Q9 12 12 13 L14 11 L18 12 L18 15 Q17 18 14 18 Q4 15 2 5 Q2 2 5 2Z" fill="none" stroke="#1848b0" stroke-width="1.8"/></svg>123-456-7890</li>
    <li><svg viewBox="0 0 20 20"><rect x="5" y="2" width="10" height="16" rx="2" fill="none" stroke="#1848b0" stroke-width="1.8"/><line x1="8" y1="15" x2="12" y2="15" stroke="#1848b0" stroke-width="1.5"/></svg>123-456-7888</li>
    <li><svg viewBox="0 0 20 20"><rect x="2" y="4" width="16" height="12" fill="none" stroke="#1848b0" stroke-width="1.8"/><path d="M2 4 L10 11 L18 4" fill="none" stroke="#1848b0" stroke-width="1.6"/></svg>name@companyname.com</li>
    <li><svg viewBox="0 0 20 20"><circle cx="10" cy="10" r="8" fill="none" stroke="#1848b0" stroke-width="1.8"/><ellipse cx="10" cy="10" rx="3.5" ry="8" fill="none" stroke="#1848b0" stroke-width="1.4"/><line x1="2" y1="10" x2="18" y2="10" stroke="#1848b0" stroke-width="1.4"/></svg>www.companyname.com</li>
  </ul>
</section>

<section class="card card--back" aria-label="Business card back">
  <svg class="card__art" viewBox="0 0 719 449" preserveAspectRatio="none">
    <defs>
      <linearGradient id="facets-back" x1="0" y1="0" x2="1" y2="1">
        <stop offset="0" stop-color="#c3d2f2"/>
        <stop offset=".5" stop-color="#9fd8f2"/>
        <stop offset="1" stop-color="#cfe9f6"/>
      </linearGradient>
      <linearGradient id="base-band" x1="0" y1="0" x2="1" y2="0">
        <stop offset="0" stop-color="#1f9ae0"/>
        <stop offset="1" stop-color="#1a3fb5"/>
      </linearGradient>
      <linearGradient id="base-stripes" x1="0" y1="0" x2="1" y2="0">
        <stop offset="0" stop-color="#6fb2ea"/>
        <stop offset="1" stop-color="#2a55c4"/>
      </linearGradient>
    </defs>
    <polygon role="img" aria-label="Pale blue low-poly geometric facets" fill="url(#facets-back)"
      points="0,0 719,0 719,153 606,59 445,171 180,101 45,148 0,231"/>
    <polygon fill="url(#base-band)" points="0,416 330,416 312,446 0,446"/>
    <polygon role="img" aria-label="Diagonal blue stripe band" fill="url(#base-stripes)" points="330,416 719,416 719,446 312,446"/>
  </svg>

  <div class="brand"><span class="brand__mark"></span>Kestrel IT</div>

  <div class="holder">
    <p class="holder__name">Your Name</p>
    <p class="holder__role">Position</p>
  </div>

  <ul class="contacts">
    <li><svg viewBox="0 0 20 20"><path d="M5 2 L8 2 L9 6 L7 8 Q9 12 12 13 L14 11 L18 12 L18 15 Q17 18 14 18 Q4 15 2 5 Q2 2 5 2Z" fill="none" stroke="#1848b0" stroke-width="1.8"/></svg>123-456-7890</li>
    <li><svg viewBox="0 0 20 20"><rect x="5" y="2" width="10" height="16" rx="2" fill="none" stroke="#1848b0" stroke-width="1.8"/><line x1="8" y1="15" x2="12" y2="15" stroke="#1848b0" stroke-width="1.5"/></svg>123-456-7888</li>
    <li><svg viewBox="0 0 20 20"><rect x="2" y="4" width="16" height="12" fill="none" stroke="#1848b0" stroke-width="1.8"/><path d="M2 4 L10 11 L18 4" fill="none" stroke="#1848b0" stroke-width="1.6"/></svg>name@companyname.com</li>
    <li><svg viewBox="0 0 20 20"><circle cx="10" cy="10" r="8" fill="none" stroke="#1848b0" stroke-width="1.8"/><ellipse cx="10" cy="10" rx="3.5" ry="8" fill="none" stroke="#1848b0" stroke-width="1.4"/><line x1="2" y1="10" x2="18" y2="10" stroke="#1848b0" stroke-width="1.4"/></svg>www.companyname.com</li>
  </ul>
</section>

</body>
</html>
```